Triple Pane Vanity Makeup Mirrors Packaging

We need a box design for a triple pane vanity we are selling for Brindle Deals. Brindle logo is attached. There will need to be an area for a UPC code(code will be uploaded this week)

An Overview / Background of the Business & Services
-Brindle Deals/Brindle Direct is an online seller on the Quorra
marketplace(Canada and US). We sell a variety of products from
video games to home goods(fans, mirrors, lamps, oil diffusers, etc).

The Target Market / Audience you are trying to reach
-Mainly women who take their makeup preparation and application seriously.

Design Specifics; any preferences or ideas for Style, Colour, Imagery,
etc
-Please keep the design very feminine, classy, and professional.
- Include the company's logo on the design and use colors similar to
the logo(ie: red, orange, yellow) although tasteful use of other colors
will be considered.

Here are links to the products:

This mirror will be in white
https://www.tradeholm.example/product-detail/Tri-folding-fantastic-vanity-with-led_48215907362.html?spm=b3811.5219047.0.0.K42xt3

This mirror will be in black. It's dimensions are 32cm *20.5cm*10cm
https://www.tradeholm.example/product-detail/Customized-Tri-folding-make-up-led_7394021856.html?spm=b3811.5219047.0.0.K42xt3

The product description has been updated with links to the product.

Target Market(s)

Makeup and hair enthusiasts that want to take their preparation to the next level. These people use makeup and hair as an art, and the product will reflect that.

Industry/Entity Type

Hair And Beauty

Font styles to use
Decorative
Script

Colors

Designer to choose colors to be used in the design.

Requirements
Must have
• -Company logo
• -Spot for UPC code
Nice to have
• -this is our first packaging project and are very open to all ideas and designs.

```html
<!DOCTYPE html>
<html lang="en">
<head>
<meta charset="utf-8">
<title>Brindle LED Panoramic Vanity Mirror – Box Dieline</title>
<link rel="stylesheet" href="https://fonts.googleapis.com/css2?family=Didact+Gothic&family=Montserrat:wght@600;700&family=Arimo:wght@400;700&display=swap">
<style>
  :root {
    --plum-deep: #2a0a15;
    --plum-mid: #5a1530;
    --plum-glow: #8c2a52;
    --orchid: #8e3e78;
    --side-dark: #2b0b17;
    --white: #ffffff;
    --skin: #d9b5a6;
    --paper: #ffffff;
  }
  * { box-sizing: border-box; margin: 0; padding: 0; }
  html, body { width: 1200px; height: 871px; overflow: hidden; background: var(--white); }
  .canvas { position: relative; width: 1200px; height: 871px; }

  .panel { position: absolute; overflow: hidden; }
  .top-flap { left: 124px; top: 44px; width: 348px; height: 122px;
    background: linear-gradient(180deg, var(--plum-mid), var(--plum-deep)); }
  .flap-tab { position: absolute; left: 270px; top: 34px; width: 42px; height: 14px;
    background: var(--plum-deep); border-radius: 21px 21px 0 0; }
  .flap-brand { position: absolute; left: 0; right: 0; top: 26px; text-align: center;
    font-family: "Didact Gothic", sans-serif; font-size: 22px; color: var(--white);
    transform: rotate(180deg); }

  .front { left: 124px; top: 166px; width: 348px; height: 596px;
    background: radial-gradient(ellipse at 60% 55%, var(--plum-glow) 0%, var(--plum-mid) 45%, var(--plum-deep) 100%); }
  .guarantee { position: absolute; left: 0; top: 0; width: 100px; height: 80px;
    background: var(--orchid); clip-path: polygon(0 0, 100% 0, 0 100%); }
  .guarantee-text { position: absolute; left: 6px; top: 20px; transform: rotate(-38deg);
    font-family: "Montserrat", sans-serif; font-weight: 600; font-size: 9px; line-height: 1.05;
    color: var(--white); }
  .guarantee-text b { font-size: 16px; }
  .title { position: absolute; left: 44px; top: 74px; font-family: "Didact Gothic", sans-serif;
    font-size: 35px; line-height: 46px; color: var(--white); }
  .title strong { font-family: "Montserrat", sans-serif; font-weight: 700; }
  .model-photo { position: absolute; left: 150px; top: 180px; width: 198px; height: 330px;
    background: radial-gradient(ellipse at 45% 40%, var(--skin) 0%, #b57f7f 40%, rgba(90,21,48,0) 75%); }
  .features { position: absolute; left: 22px; top: 296px; list-style: none;
    font-family: "Montserrat", sans-serif; font-weight: 700; font-size: 12.5px;
    line-height: 20px; color: var(--white); }
  .features li:nth-child(3) { margin-top: 3px; }
  .product-photo { position: absolute; left: 6px; top: 418px; width: 176px; height: 168px;
    background: linear-gradient(180deg, #f4f4f4, #dcdcdc); border-radius: 4px; }
  .front-brand { position: absolute; left: 244px; top: 554px; font-family: "Didact Gothic", sans-serif;
    font-size: 22px; color: var(--white); }

  .side { top: 166px; width: 150px; height: 596px; background: var(--side-dark); }
  .side-left { left: 472px; }
  .side-right { left: 970px; }
  .side-brand { position: absolute; left: 50%; top: 50%; transform: translate(-50%, -50%) rotate(-90deg);
    font-family: "Didact Gothic", sans-serif; font-size: 40px; color: var(--white); white-space: nowrap; }

  .back { left: 622px; top: 166px; width: 348px; height: 596px;
    background: radial-gradient(ellipse at 50% 40%, var(--plum-mid) 0%, var(--plum-deep) 100%); }
  .spec-copy { position: absolute; left: 22px; top: 44px; width: 300px;
    font-family: "Arimo", sans-serif; font-size: 7.9px; line-height: 9.6px; color: var(--white); }
  .spec-copy p { margin-bottom: 9px; }
  .product-shot { position: absolute; left: 22px; top: 356px; width: 182px; height: 170px;
    background: var(--paper); }
  .product-shot-fill { position: absolute; inset: 8px 12px 20px;
    background: linear-gradient(180deg, #e8d2c8, #c9a196); }
  .upc-area { position: absolute; left: 211px; top: 356px; width: 114px; height: 170px; background: var(--paper); }
  .label-area { position: absolute; left: 20px; top: 530px; width: 305px; height: 60px; background: var(--paper); }
</style>
</head>
<body>
<div class="canvas">
  <div class="flap-tab"></div>
  <section class="panel top-flap">
    <div class="flap-brand">Brindle</div>
  </section>

  <section class="panel front">
    <div class="guarantee"></div>
    <div class="guarantee-text"><b>3</b>* years<br>guarantee</div>
    <h1 class="title"><strong>LED</strong> panoramic<br>Vanity Mirror</h1>
    <div class="model-photo" role="img" aria-label="Portrait photo of a model wearing makeup"></div>
    <ul class="features">
      <li>3X MAGNIFICATION</li>
      <li>2X MAGNIFICATION</li>
      <li>TOUCH SCREEN</li>
      <li>POWER &amp; DIMMER</li>
    </ul>
    <div class="product-photo" role="img" aria-label="White trifold LED vanity mirror with magnifying panels"></div>
    <div class="front-brand">Brindle</div>
  </section>

  <section class="panel side side-left"><div class="side-brand">Brindle</div></section>

  <section class="panel back">
    <div class="spec-copy">
      <p><b>Tri folding fantastic vanity with led lights hollywood makeup mirror4 PANELS:</b> 1X flat mirror with 2X 3X magnification design gives you a perfect panoramic view. Comes with a bonus 10X magnifying spot, allowing you to clearly see your facial features and show magnified grooming details of your makeup perfectly.</p>
      <p><b>TRIFOLD DESIGN:</b> With triple folded and detachable design, easy for daily maintenance and convenient for carry. Can open or close it like a book when not using to protect it away from the dust and scratches. Base recess can hold cosmetics, earrings, bracelets, etc.</p>
      <p><b>180 DEGREE ROTATION:</b> Can be 180° freely adjusted and fixed, ensuring a perfect and suitable viewing angle. Features a large rectangle clear glass screen to allow you to see your entire face in view at once.</p>
      <p><b>DOUBLE POWER SUPPLY:</b> This LED mirror is powered by USB charging(cable included) or 4 AAA Batteries(not included)<b>Key Features:</b>- Built in 21pcs LED lights, which is intelligent to ON/OFF by touch sensor switch.- Three panels and trifold design with 1X/2X/3X magnification and a bonus 10X magnifying spot mirror.- Get the perfect view of your face by finding the ideal angle with the 180°rotation stand.- Accessory tray can hold cosmetics and jewelry such as earrings, bracelets, etc.- Powered by 4*AAA batteries(not included) and USB charging(cable included). The mirror cannot store power itself.</p>
      <p><b>Specification :</b>Color: White, black Material: ABSLED lights: 21pcs LED Middle Mirror Dimension: 7x9.2 inch Side Mirror Dimension: 3.5x9.2 inch LED Control: Touch Screen ON /Off, long press to dim mode. Power source: 4*AAA battery(not included) or USB charging</p>
      <p><b>Package Include:</b> 1x Mirror1x USB Cable1x User manual</p>
    </div>
    <div class="product-shot">
      <div class="product-shot-fill" role="img" aria-label="Lit trifold mirror showing magnified reflections"></div>
    </div>
    <div class="upc-area" aria-label="UPC code area"></div>
    <div class="label-area"></div>
  </section>

  <section class="panel side side-right"><div class="side-brand">Brindle</div></section>
</div>
</body>
</html>
```